Startup photo studio needs full suite design (logo, business cards, etc) starting with a website.

We need a website designed for a startup photo studio in the Sacramento area called Silver Lantern Photo Studio. We do portrait work, specializing in the male form and are looking to get into editorial. We would also like to be able to sell prints, posters and canvasses of our work. I would like an elegant but fun design. One of the most important things a portrait photographer needs is the trust of the model. The website would convey honesty, friendliness and warmth as well. I have a domain name with NetHarbor, silverlanternstudio.example email address should be my name with that domain.

Target Market(s)

Art enthusiasts, business portraits, online dating photos

Industry/Entity Type

Professional Photography

Contact Information for Business Card

Simple please. Just logo and contact info. Phone, email, website. no address required

Logo Text

Silver Lantern Photo Studio --- every frame glows

Number of Pages Required

3 page

Font styles to use
Sans Serif

Colors

Designer to choose colors to be used in the design.

Requirements
Must have
• Simple clean design.
Nice to have
• Somehow one of my photos in the design? maybe not...
Should not have
• No weddings!

```html
<!DOCTYPE html>
<html lang="en">
<head>
<meta charset="utf-8">
<title>Silver Lantern Photo Studio</title>
<link href="https://fonts.googleapis.com/css2?family=Montserrat:wght@400;600;700&display=swap" rel="stylesheet">
<style>
:root{
  --gold:#f2b035;
  --ink:#222;
  --dark:#151515;
  --slate:#2b2d33;
  --muted:#777;
  --paper:#fff;
  --backdrop:#e9e9e9;
}
*{margin:0;padding:0;box-sizing:border-box}
html,body{width:1200px;height:1200px;overflow:hidden;background:var(--backdrop);font-family:'Montserrat',sans-serif}
.page{position:absolute;left:494px;top:8px;width:263px;height:1480px;transform:scale(.8);transform-origin:0 0;background:var(--paper);box-shadow:0 0 18px rgba(0,0,0,.35);overflow:hidden}
.abs{position:absolute}
.t{position:absolute;line-height:1.25;color:var(--ink)}
.tiny{font-size:2.6px;color:var(--muted);line-height:1.5}
.gold{color:var(--gold)}
.btn{position:absolute;background:var(--gold);color:#222;font-size:2.8px;text-align:center;border-radius:6px;font-weight:600}
.photo{position:absolute}
.h2{position:absolute;left:0;width:263px;text-align:center;font-size:7px;color:#333;letter-spacing:.3px;white-space:nowrap}
.h2 b{color:var(--gold);font-weight:700}

.nav{left:0;top:0;width:263px;height:18px;background:var(--dark);border-bottom:1.5px solid var(--gold)}
.brand{position:absolute;left:12px;top:6px;font-size:4.5px;color:var(--gold);font-weight:600;white-space:nowrap}
.menu{position:absolute;right:8px;top:0;display:flex;font-size:2.6px;color:#ddd;height:18px;align-items:center;white-space:nowrap}
.menu span{padding:0 3.2px;height:18px;line-height:18px}
.menu .on{background:var(--gold);color:#222}

.hero{left:0;top:18px;width:263px;height:120px;background:linear-gradient(100deg,#5a1c10 0%,#b2471d 35%,#8a3a3a 60%,#3d3056 100%)}
.hero .line1{left:13px;top:23px;font-size:11px;color:#fff}
.hero .line2{left:13px;top:38px;font-size:16.5px;color:var(--gold);font-weight:700}
.hero .line3{left:13px;top:61px;font-size:7px;color:#fff;letter-spacing:2px;white-space:nowrap}
.pager{left:227px;top:42px;width:6px;height:36px;border:1px solid var(--gold);border-radius:3px}

.frame{position:absolute;border:1px solid #999}
.card-img{position:absolute;width:70px;height:70px}
.svc-title{position:absolute;top:431px;width:74px;text-align:center;font-size:3.6px;color:#555;white-space:nowrap}
.price{position:absolute;top:1063px;width:77px;height:135px;background:var(--gold)}
.price .top{position:absolute;left:0;top:0;width:100%;height:36px;background:var(--slate)}
.price .badge{position:absolute;left:22px;top:10px;width:33px;height:33px;border-radius:50%;background:var(--slate);border:1.5px solid var(--gold);color:#fff;font-size:5px;text-align:center;padding-top:9px;font-weight:700}
.price .badge small{display:block;font-size:2px;font-weight:400;margin-bottom:1px}
.price ul{position:absolute;left:4px;right:4px;top:48px;list-style:none;font-size:2.3px;text-align:center;line-height:2.1;color:#333}
.price .buy{position:absolute;left:20px;top:112px;width:37px;height:6px;background:var(--slate);color:#fff;font-size:2.4px;text-align:center;line-height:6px;border-radius:4px}
.price.alt{background:var(--slate)}
.price.alt .top{background:var(--gold)}
.price.alt ul{color:#eee}
.price.alt .buy{background:var(--gold);color:#222}
.filters{left:74px;top:698px;display:flex;gap:1px}
.filters span{font-size:2.2px;background:#333;color:#eee;padding:1.2px 3px;white-space:nowrap}
.filters .on{background:var(--gold);color:#222}
.field{position:absolute;left:155px;width:96px;height:8px;border:.5px solid #666}
.dots{display:flex;gap:2px}
.dots i{width:5px;height:5px;border-radius:50%;background:#222;display:block}
</style>
</head>
<body>
<div class="page">

  <header class="abs nav">
    <div class="brand">Silver Lantern</div>
    <nav class="menu"><span class="on">HOME</span><span>ABOUT US</span><span>SERVICES</span><span>PORTFOLIO</span><span>FEEDBACK</span><span>PRICING</span><span>CONTACT US</span></nav>
  </header>

  <section class="abs hero" role="img" aria-label="Photographer holding a camera to her face, warm orange and violet tones">
    <div class="t line1">We Are Best</div>
    <div class="t line2">PHOTOGRAPHER</div>
    <div class="t line3">&amp; Award Winner 2016</div>
    <div class="abs pager"></div>
    <div class="btn" style="left:13px;top:101px;width:44px;height:8px;line-height:8px">VIEW OUR WORK</div>
  </section>

  <div class="frame" style="left:12px;top:158px;width:56px;height:1px;border:none;border-top:1px solid #999"></div>
  <div class="frame" style="left:12px;top:158px;width:1px;height:62px;border:none;border-left:1px solid #999"></div>
  <div class="frame" style="left:128px;top:226px;width:1px;height:62px;border:none;border-left:1px solid #999"></div>
  <div class="frame" style="left:70px;top:288px;width:59px;height:1px;border:none;border-top:1px solid #999"></div>
  <div class="photo" style="left:18px;top:163px;width:106px;height:120px;background:linear-gradient(135deg,#5a3424,#c98e6e 55%,#ead6c8)" role="img" aria-label="Portrait of a curly-haired woman with a camera"></div>
  <div class="t" style="left:155px;top:158px;font-size:6px;color:#333">[ ABOUT <b class="gold">US</b> ]</div>
  <div class="t" style="left:155px;top:173px;font-size:3.6px;width:95px">We are excellent photographer and creative designer.</div>
  <div class="t tiny" style="left:155px;top:187px;width:96px">Silver Lantern began as a small studio with a love of honest light. For years we have made portraits that feel warm, calm and true to the people in them.</div>
  <div class="t tiny" style="left:155px;top:206px;width:96px">Every session starts with a conversation. We listen first, then shape the light around you so each frame feels relaxed, natural and entirely your own story.</div>
  <div class="t" style="left:155px;top:253px;font-size:3px;font-weight:600">Silver Lantern Studio</div>
  <div class="abs dots" style="left:155px;top:262px"><i></i><i></i><i></i><i></i></div>

  <div class="h2" style="top:307px">[ WE PROVIDE <b>THE BEST SERVICES</b> ]</div>
  <div class="t tiny" style="left:32px;top:322px;width:200px;text-align:center">Simple sample text for the services intro, describing the portrait sessions we offer and the friendly, honest way we work.</div>
  <div class="frame" style="left:12px;top:344px;width:74px;height:76px;border-right:none;border-bottom:none"></div>
  <div class="card-img" style="left:16px;top:348px;background:linear-gradient(135deg,#c8b8a0,#6a5a48 60%,#222)" role="img" aria-label="Editorial portrait of a man in a studio"></div>
  <div class="frame" style="left:94px;top:344px;width:74px;height:76px;border-right:none;border-bottom:none"></div>
  <div class="card-img" style="left:97px;top:348px;background:linear-gradient(135deg,#d9d9df,#8a8a92 55%,#3a3a44)" role="img" aria-label="Business team in an office"></div>
  <div class="frame" style="left:175px;top:344px;width:74px;height:76px;border-right:none;border-bottom:none"></div>
  <div class="card-img" style="left:178px;top:348px;background:linear-gradient(135deg,#4a6a3c,#2b2b2b 50%,#b03030)" role="img" aria-label="Seated portrait outdoors"></div>
  <div class="svc-title" style="left:13px">Editorial Photography</div>
  <div class="svc-title" style="left:95px">Corporate Photography</div>
  <div class="svc-title" style="left:176px">Portraits Photography</div>
  <div class="t tiny" style="left:13px;top:441px;width:74px;text-align:center">Short sample text about this session type, the time we spend together and what you take home.</div>
  <div class="t tiny" style="left:95px;top:441px;width:74px;text-align:center">Short sample text about this session type, the time we spend together and what you take home.</div>
  <div class="t tiny" style="left:176px;top:441px;width:74px;text-align:center">Short sample text about this session type, the time we spend together and what you take home.</div>
  <div class="t" style="left:13px;top:463px;width:74px;text-align:center;font-size:2.4px;color:var(--gold)">Read More</div>
  <div class="t" style="left:95px;top:463px;width:74px;text-align:center;font-size:2.4px;color:var(--gold)">Read More</div>
  <div class="t" style="left:176px;top:463px;width:74px;text-align:center;font-size:2.4px;color:var(--gold)">Read More</div>

  <section class="abs" style="left:0;top:488px;width:263px;height:150px;background:linear-gradient(90deg,#111,#1d1b17)">
    <div class="t" style="left:12px;top:28px;font-size:6.5px;color:#fff">[</div>
    <div class="t" style="left:105px;top:28px;font-size:6.5px;color:#fff">]</div>
    <div class="t" style="left:20px;top:29px;width:80px;text-align:center;font-size:6px;color:#fff">OUR AWSOME<br><b class="gold">WORK</b></div>
    <div class="t tiny" style="left:12px;top:62px;width:96px;color:#bbb">Sample text about our recent shoots, the people we met and the light we chased across every location.</div>
    <div class="t tiny" style="left:12px;top:83px;width:96px;color:#bbb">More sample text describing the editorial direction of the studio and the prints now on offer.</div>
    <div class="btn" style="left:12px;top:115px;width:46px;height:8px;line-height:8px">SEE MORE WORK</div>
    <div class="abs" style="left:128px;top:29px;width:110px;height:110px;border-radius:50%;border:1.5px solid var(--gold);background:linear-gradient(135deg,#8a6c3c,#cfae74 40%,#3a3140 60%,#6a4a6a)" role="img" aria-label="Collage of editorial portraits in a circle"></div>
  </section>

  <div class="h2" style="top:659px">[ OUR AWESOME <b>PORTFOLIO</b> ]</div>
  <div class="t tiny" style="left:32px;top:676px;width:200px;text-align:center">Sample text introducing the portfolio, a selection of portrait, editorial and studio work.</div>
  <div class="abs filters"><span class="on">CATEGORIES</span><span>PORTRAITS</span><span>EDITORIAL</span><span>STUDIO ARTISTIC</span></div>
  <div class="photo" style="left:2px;top:715px;width:60px;height:63px;background:linear-gradient(160deg,#8aa,#334 70%)" role="img" aria-label="Studio portrait"></div>
  <div class="photo" style="left:68px;top:715px;width:125px;height:63px;background:linear-gradient(120deg,#6a4a2a,#e3c9a8 45%,#3a3a3a)" role="img" aria-label="Two friends laughing in a portrait"></div>
  <div class="photo" style="left:199px;top:715px;width:61px;height:63px;background:linear-gradient(160deg,#9ab,#c55 60%,#335)" role="img" aria-label="Group of dancers"></div>
  <div class="photo" style="left:2px;top:784px;width:60px;height:63px;background:linear-gradient(160deg,#ccc,#333 65%)" role="img" aria-label="Fashion group"></div>
  <div class="photo" style="left:68px;top:784px;width:60px;height:63px;background:linear-gradient(160deg,#bbb,#444 65%)" role="img" aria-label="Group of men"></div>
  <div class="photo" style="left:134px;top:784px;width:59px;height:63px;background:linear-gradient(180deg,#111,#2a6fd0 65%,#1a3f80)" role="img" aria-label="Man in blue tank top"></div>
  <div class="photo" style="left:199px;top:784px;width:61px;height:63px;background:linear-gradient(180deg,#111,#a07a4a 55%,#2a1c10)" role="img" aria-label="Male figure study"></div>

  <section class="abs" style="left:0;top:855px;width:263px;height:149px;background:linear-gradient(120deg,#151515,#3a2a1e 70%,#1a1410)">
    <div class="h2" style="top:19px;color:#fff">[ CLIENT <b>FEEDBACK</b> ]</div>
    <div class="t tiny" style="left:32px;top:36px;width:200px;text-align:center;color:#bbb">Sample text from happy clients about feeling welcome, safe and at ease in front of the lens.</div>
    <div class="frame" style="left:13px;top:58px;width:74px;height:82px;border-color:#888"></div>
    <div class="photo" style="left:18px;top:63px;width:68px;height:65px;background:linear-gradient(135deg,#9aa,#8a2a2a 60%,#3a1a1a)" role="img" aria-label="Client portrait"></div>
    <div class="t" style="left:113px;top:81px;font-size:3.6px;color:var(--gold)">DANA WHITFIELD</div>
    <div class="t" style="left:113px;top:87px;font-size:2.4px;color:#aaa">Portrait client</div>
    <div class="t tiny" style="left:113px;top:95px;width:140px;color:#ccc">The studio felt warm from the first minute. I was nervous, yet they made me laugh and the photos look like the best version of me. I would gladly come back for new prints.</div>
    <div class="t" style="left:113px;top:121px;font-size:4px;color:var(--gold);letter-spacing:1px">★★★★★</div>
    <div class="t" style="left:4px;top:100px;font-size:5px;color:#fff">‹</div>
    <div class="t" style="left:255px;top:100px;font-size:5px;color:#fff">›</div>
  </section>

  <div class="h2" style="top:1025px">[ PURCHASE <b>A PACKAGE</b> ]</div>
  <div class="t tiny" style="left:32px;top:1042px;width:200px;text-align:center">Sample text describing our packages, each with edited images, prints and an online gallery.</div>
  <div class="price" style="left:9px"><div class="top"></div><div class="badge"><small>PROFESSIONAL</small>$450</div>
    <ul><li>✔ Final images fully edited</li><li>✔ Print release for personal use</li><li>✔ CD with all high resolution images</li><li>✔ 90 minute session at your location</li><li>✔ Online password gallery</li><li>✔ Travel fees may apply</li></ul><div class="buy">Purchase Now</div></div>
  <div class="price" style="left:92px"><div class="top"></div><div class="badge"><small>SPECIAL</small>$450</div>
    <ul><li>✔ Final images fully edited</li><li>✔ Print release for personal use</li><li>✔ CD with all high resolution images</li><li>✔ 90 minute session at your location</li><li>✔ Online password gallery</li><li>✔ Travel fees may apply</li></ul><div class="buy">Purchase Now</div></div>
  <div class="price alt" style="left:175px"><div class="top"></div><div class="badge" style="background:var(--gold);color:#222;border-color:var(--slate)"><small>GROUP</small>$450</div>
    <ul><li>✔ Final images fully edited</li><li>✔ Print release for personal use</li><li>✔ CD with all high resolution images</li><li>✔ 90 minute session at your location</li><li>✔ Online password gallery</li><li>✔ Travel fees may apply</li></ul><div class="buy">Purchase Now</div></div>

  <section class="abs" style="left:0;top:1218px;width:263px;height:87px;background:var(--gold)">
    <div class="h2" style="top:20px">[ 5000K PEOPLE LIKE <b style="color:#222">US</b> ]</div>
    <div class="t tiny" style="left:32px;top:36px;width:200px;text-align:center;color:#fff">Sample text inviting visitors to join our list for new work, print releases and studio news.</div>
    <div class="abs" style="left:71px;top:59px;width:84px;height:8px;background:#fff;border-radius:4px 0 0 4px;font-size:2.4px;color:#aaa;text-align:center;line-height:8px">Enter Your Email</div>
    <div class="abs" style="left:154px;top:59px;width:36px;height:8px;background:var(--slate);border-radius:0 4px 4px 0;font-size:2.4px;color:#fff;text-align:center;line-height:8px">SUBSCRIBE</div>
  </section>

  <section class="abs" style="left:0;top:1305px;width:263px;height:162px;background:var(--slate)">
    <div class="abs" style="left:0;top:0;width:263px;height:162px;background:linear-gradient(135deg,#33363d,#262830)" role="img" aria-label="Faint city map of the studio area"></div>
    <div class="h2" style="top:20px;color:#fff">[ CONTACTS <b>US</b> ]</div>
    <div class="t tiny" style="left:32px;top:36px;width:200px;text-align:center;color:#bbb">Sample text asking visitors to reach out to book a session or order prints of our work.</div>
    <div class="brand" style="left:9px;top:63px">Silver Lantern</div>
    <div class="t tiny" style="left:9px;top:78px;color:#ccc">Sacramento<br>California, USA</div>
    <div class="t tiny" style="left:9px;top:90px;color:#ccc">Email: dana@silverlanternstudio.example<br>Phone: (916) 555-0142</div>
    <div class="abs dots" style="left:9px;top:111px;gap:3px"><i style="width:3px;height:3px;background:#888"></i><i style="width:3px;height:3px;background:#888"></i><i style="width:3px;height:3px;background:#888"></i><i style="width:3px;height:3px;background:#888"></i><i style="width:3px;height:3px;background:#888"></i></div>
    <div class="field" style="top:65px"></div>
    <div class="field" style="top:75px"></div>
    <div class="field" style="top:85px"></div>
    <div class="field" style="top:95px"></div>
    <div class="field" style="top:105px;height:24px"></div>
    <div class="btn" style="left:155px;top:136px;width:36px;height:8px;line-height:8px;border-radius:0">SEND MESSAGE</div>
  </section>

  <footer class="abs" style="left:0;top:1467px;width:263px;height:13px;background:#0d0d0d">
    <div class="t" style="left:0;top:5px;width:263px;text-align:center;font-size:2.4px;color:#999">Copyright © 2017 All Right Reserved. Silver Lantern Photo Studio</div>
    <div class="abs" style="left:251px;top:2px;width:8px;height:9px;background:var(--gold)"></div>
  </footer>

</div>
</body>
</html>
```